Concierge Healthcare Business Card Design and Logo

We need a logo and business card design for a new company called "Sound Harbor". We will provide concierge audiological care, hearing aids, hearing exams, custom hearing protection etc to patients in the comfort of their homes and offices. We would like a sleek and modern design preferably with an Ear related logo.

Target Market(s)

People with hearing loss, Hunters, Musicians
My usual clientele are older individuals so usually 50+ years old

Industry/Entity Type

Health Care

Contact Information for Business Card

Delia Franks, AuD
Audiologist
512-648-2917
soundharbor@mailnest.com
www.soundharbor-example.com

Logo Text

Sound Harbor

Number of Pages Required

3 page

```html
<!DOCTYPE html>
<html lang="en">
<head>
<meta charset="utf-8">
<title>Sound Harbor — Business Card</title>
<link rel="stylesheet" href="https://fonts.googleapis.com/css2?family=Lato:wght@400;700&family=Quicksand:wght@300;400&display=swap">
<style>
  :root {
    --brand-red: #e31b23;
    --card-white: #ffffff;
    --ink: #1d1d1f;
    --ink-soft: #5a5a5e;
    --wordmark-grey: #3a3a3d;
    --backdrop: #e6e6e8;
  }
  * { box-sizing: border-box; margin: 0; padding: 0; }
  html, body {
    width: 1200px;
    height: 790px;
    overflow: hidden;
    background: var(--backdrop);
  }
  .canvas {
    position: relative;
    width: 1200px;
    height: 790px;
    display: flex;
    align-items: center;
    justify-content: center;
    gap: 60px;
  }
  .card {
    position: relative;
    width: 500px;
    height: 286px;
    border-radius: 3px;
    box-shadow: 0 10px 30px rgba(0,0,0,0.12);
  }
  .card--front { background: var(--card-white); }
  .card--back {
    background: var(--brand-red);
    display: flex;
    align-items: center;
    justify-content: center;
  }

  .brand {
    position: absolute;
    left: 40px;
    top: 44px;
    display: flex;
    align-items: center;
    gap: 14px;
  }
  .brand__square {
    width: 62px;
    height: 62px;
    border-radius: 8px;
    background: var(--brand-red);
  }
  .brand__name {
    font-family: "Quicksand", sans-serif;
    font-weight: 300;
    font-size: 36px;
    letter-spacing: 0.5px;
    color: var(--wordmark-grey);
    text-transform: lowercase;
  }

  .contact {
    position: absolute;
    left: 228px;
    top: 140px;
    font-family: "Lato", sans-serif;
    color: var(--ink);
  }
  .contact__name { font-size: 14px; font-weight: 400; }
  .contact__role { font-size: 13px; color: var(--ink-soft); margin-bottom: 8px; }
  .contact__list { list-style: none; }
  .contact__item {
    display: flex;
    align-items: center;
    gap: 7px;
    font-size: 13px;
    line-height: 19px;
  }
  .contact__icon { width: 10px; height: 10px; flex: none; }

  .back__name {
    font-family: "Quicksand", sans-serif;
    font-weight: 300;
    font-size: 40px;
    color: var(--card-white);
    text-transform: lowercase;
    letter-spacing: 0.5px;
  }
</style>
</head>
<body>
<main class="canvas">
  <section class="card card--front" aria-label="Business card front">
    <div class="brand">
      <span class="brand__square"></span>
      <span class="brand__name">Sound Harbor</span>
    </div>
    <div class="contact">
      <p class="contact__name">Delia Franks, AuD</p>
      <p class="contact__role">Audiologist</p>
      <ul class="contact__list">
        <li class="contact__item">
          <svg class="contact__icon" viewBox="0 0 10 10" aria-hidden="true">
            <rect x="2" y="0.5" width="6" height="9" rx="1" fill="none" stroke="#e31b23" stroke-width="1.2"/>
            <circle cx="5" cy="7.8" r="0.7" fill="#e31b23"/>
          </svg>
          512-648-2917
        </li>
        <li class="contact__item">
          <svg class="contact__icon" viewBox="0 0 10 10" aria-hidden="true">
            <rect x="0.5" y="2" width="9" height="6.5" rx="1" fill="#e31b23"/>
            <path d="M1 2.6 L5 5.6 L9 2.6" fill="none" stroke="#fff" stroke-width="0.9"/>
          </svg>
          soundharbor@mailnest.com
        </li>
        <li class="contact__item">
          <svg class="contact__icon" viewBox="0 0 10 10" aria-hidden="true">
            <circle cx="5" cy="5" r="4.5" fill="#e31b23"/>
            <path d="M0.8 5 H9.2 M5 0.6 V9.4 M5 0.6 C2.5 3 2.5 7 5 9.4 M5 0.6 C7.5 3 7.5 7 5 9.4" fill="none" stroke="#fff" stroke-width="0.6"/>
          </svg>
          www.soundharbor-example.com
        </li>
      </ul>
    </div>
  </section>

  <section class="card card--back" aria-label="Business card back">
    <span class="back__name">Sound Harbor</span>
  </section>
</main>
</body>
</html>
```